Unique Elegant Stationary Set

Prepare a unique eye catching stationary set consisting of :
(1) Letterhead
(2) A3 Envelope
(3) Business Card
(4) Email Signature Banner

Package to be elegant, modern, and designers not only to think of design or colors but also materials could make a big difference, embossing, debossing, glossy, matt ....etc.

I attached both our new logos (Stacked or Linear) noting you may use any of them but you cant modify anything in the logos. Also attached our final draft portfolio to see what type of projects we work on and i also have here a glimboard page link showing the direction we want: https://www.glimboard.example/ravelkoton/business-card-design/

Target Market(s)

VVIP / Elite Developers

Industry/Entity Type

Architecture

Font styles to use
Sans Serif
Other font styles liked:
• unitext

Requirements
Should not have
• too many colors, or being busy in general. We want something pleasing to the eye

```html
<!DOCTYPE html>
<html lang="en">
<head>
<meta charset="utf-8">
<title>Kelto Studio — Stationery Set</title>
<link rel="stylesheet" href="https://fonts.googleapis.com/css2?family=Outfit:wght@300;400;600;700&display=swap">
<style>
  :root {
    --brand-red: #c1222a;
    --ink-black: #0b0b0b;
    --paper-white: #ffffff;
    --logo-grey: #4a4a4a;
    --backdrop: #b3b3b3;
    --drop-shadow: 7px 9px 12px rgba(0,0,0,.38);
    --type: "Outfit", Arial, sans-serif;
  }
  html, body {
    margin: 0;
    width: 940px;
    height: 1200px;
    overflow: hidden;
    background: var(--backdrop);
    font-family: var(--type);
  }
  .stationery-board {
    position: relative;
    width: 960px;
    height: 1226px;
    transform: scale(0.9792);
    transform-origin: 0 0;
  }
  .piece {
    position: absolute;
    box-shadow: var(--drop-shadow);
    overflow: hidden;
  }
  .wordmark {
    position: absolute;
    margin: 0;
    font-family: var(--type);
    font-weight: 700;
    white-space: nowrap;
    line-height: 1;
    display: flex;
    align-items: center;
    gap: .22em;
  }
  .wordmark .mark-square {
    width: .32em;
    height: .32em;
    background: currentColor;
    display: inline-block;
  }
  .contact-list {
    position: absolute;
    list-style: none;
    margin: 0;
    padding: 0;
  }
  .contact-list li {
    display: flex;
    align-items: center;
  }
  .contact-list svg { flex: none; fill: currentColor; }

  /* Envelope */
  .envelope {
    left: 48px; top: 43px; width: 524px; height: 370px;
    background: var(--brand-red);
    color: var(--paper-white);
  }
  .envelope .wordmark { left: 40px; top: 52px; font-size: 49px; color: var(--paper-white); }
  .envelope .contact-list { left: 40px; top: 276px; font-size: 13px; font-weight: 400; }
  .envelope .contact-list li { height: 18px; gap: 6px; }
  .envelope .contact-list svg { width: 10px; height: 10px; }
  .envelope .corner-cut { position: absolute; left: 0; top: 0; }

  /* Business card front */
  .card-front {
    left: 599px; top: 43px; width: 301px; height: 171px;
    background: var(--ink-black);
    color: var(--paper-white);
  }
  .card-front .logo-band {
    position: absolute; left: 0; top: 0; width: 301px; height: 78px;
    background: var(--paper-white);
  }
  .card-front .wordmark { left: 28px; top: 26px; font-size: 26px; color: var(--ink-black); }
  .card-front .holder-name {
    position: absolute; left: 42px; top: 114px; margin: 0;
    font-size: 14px; font-weight: 600;
  }
  .card-front .divider {
    position: absolute; left: 141px; top: 108px; width: 1px; height: 36px;
    background: #555;
  }
  .card-front .contact-list { left: 160px; top: 107px; font-size: 8.5px; }
  .card-front .contact-list li { height: 12px; gap: 5px; }
  .card-front .contact-list svg { width: 7px; height: 7px; }

  /* Business card back */
  .card-back {
    left: 599px; top: 243px; width: 301px; height: 170px;
    background: var(--paper-white);
  }
  .card-back .wordmark { left: 36px; top: 81px; font-size: 25px; color: var(--brand-red); }

  /* Letterhead */
  .letterhead {
    left: 48px; top: 441px; width: 524px; height: 742px;
    background: var(--paper-white);
    color: var(--ink-black);
  }
  .letterhead .wordmark { left: 49px; top: 56px; font-size: 27px; color: var(--ink-black); }
  .letterhead .contact-list { left: 320px; top: 50px; font-size: 15px; font-weight: 400; }
  .letterhead .contact-list li { height: 21px; gap: 8px; }
  .letterhead .contact-list svg { width: 11px; height: 11px; }
  .letterhead .footer-band { position: absolute; left: 0; bottom: 0; }

  /* Email signature */
  .email-signature {
    left: 234px; top: 779px; width: 678px; height: 156px;
    background: var(--paper-white);
    display: flex;
  }
  .email-signature .logo-side { position: relative; width: 366px; height: 100%; }
  .email-signature .wordmark { left: 57px; top: 60px; font-size: 33px; color: var(--brand-red); }
  .email-signature .details-side {
    position: relative; flex: 1; height: 100%;
    background: var(--brand-red); color: var(--paper-white);
  }
  .email-signature .holder-name {
    position: absolute; left: 86px; top: 30px; margin: 0;
    font-size: 20px; font-weight: 600;
  }
  .email-signature .contact-list { left: 86px; top: 73px; font-size: 13px; }
  .email-signature .contact-list li { height: 18px; gap: 7px; }
  .email-signature .contact-list svg { width: 9px; height: 9px; }
</style>
</head>
<body>
<svg width="0" height="0" style="position:absolute" aria-hidden="true">
  <symbol id="icon-phone" viewBox="0 0 24 24">
    <path d="M6.6 10.8a15.1 15.1 0 0 0 6.6 6.6l2.2-2.2a1 1 0 0 1 1-.25 11.4 11.4 0 0 0 3.6.57 1 1 0 0 1 1 1V20a1 1 0 0 1-1 1A17 17 0 0 1 3 4a1 1 0 0 1 1-1h3.5a1 1 0 0 1 1 1c0 1.25.2 2.45.57 3.57a1 1 0 0 1-.25 1z"/>
  </symbol>
  <symbol id="icon-mail" viewBox="0 0 24 24">
    <path d="M2 5h20v14H2z M3.5 6.5 12 12.5l8.5-6z" fill-rule="evenodd"/>
  </symbol>
  <symbol id="icon-globe" viewBox="0 0 24 24">
    <path d="M12 2a10 10 0 1 0 0 20 10 10 0 0 0 0-20zm0 2.2c.9 1.2 1.6 2.8 1.9 4.8h-3.8c.3-2 1-3.6 1.9-4.8zM4.3 11h3.8a17 17 0 0 0 .2 2H4.3a8 8 0 0 1 0-2zm15.4 0a8 8 0 0 1 0 2h-4a17 17 0 0 0 .2-2zM10 11h4a15 15 0 0 1-.1 2h-3.8A15 15 0 0 1 10 11zm.1 4h3.8c-.3 2-1 3.6-1.9 4.8-.9-1.2-1.6-2.8-1.9-4.8z"/>
  </symbol>
</svg>

<main class="stationery-board">

  <section class="piece envelope" aria-label="Envelope">
    <p class="wordmark">KELTO STUDIO<span class="mark-square"></span></p>
    <ul class="contact-list">
      <li><svg><use href="#icon-phone"/></svg><span>+43 123 456 7890</span></li>
      <li><svg><use href="#icon-mail"/></svg><span>email@domain.com</span></li>
      <li><svg><use href="#icon-globe"/></svg><span>www.keltostudio.com</span></li>
    </ul>
    <svg class="corner-cut" width="524" height="370" viewBox="0 0 524 370" aria-hidden="true">
      <polygon points="186,370 254,279 372,296 524,279 524,370" fill="var(--paper-white)"/>
      <polygon points="186,370 254,279 524,334 272,307" fill="var(--ink-black)"/>
    </svg>
  </section>

  <section class="piece card-front" aria-label="Business card front">
    <div class="logo-band">
      <p class="wordmark">KELTO STUDIO<span class="mark-square"></span></p>
    </div>
    <p class="holder-name">Your Name</p>
    <span class="divider"></span>
    <ul class="contact-list">
      <li><svg><use href="#icon-phone"/></svg><span>+43 123 456 7890</span></li>
      <li><svg><use href="#icon-mail"/></svg><span>email@domain.com</span></li>
      <li><svg><use href="#icon-globe"/></svg><span>www.keltostudio.com</span></li>
    </ul>
  </section>

  <section class="piece card-back" aria-label="Business card back">
    <p class="wordmark">KELTO STUDIO<span class="mark-square"></span></p>
  </section>

  <section class="piece letterhead" aria-label="Letterhead">
    <p class="wordmark">KELTO STUDIO</p>
    <ul class="contact-list">
      <li><svg><use href="#icon-phone"/></svg><span>+43 123 456 7890</span></li>
      <li><svg><use href="#icon-mail"/></svg><span>email@domain.com</span></li>
      <li><svg><use href="#icon-globe"/></svg><span>www.keltostudio.com</span></li>
    </ul>
    <svg class="footer-band" width="524" height="90" viewBox="0 0 524 90" aria-hidden="true">
      <polygon points="0,47 92,47 130,70 382,70 524,2 524,90 0,90" fill="var(--brand-red)"/>
      <polygon points="0,64 72,64 117,90 0,90" fill="var(--paper-white)"/>
    </svg>
  </section>

  <section class="piece email-signature" aria-label="Email signature banner">
    <div class="logo-side">
      <p class="wordmark">KELTO STUDIO</p>
    </div>
    <div class="details-side">
      <p class="holder-name">Your Name</p>
      <ul class="contact-list">
        <li><svg><use href="#icon-phone"/></svg><span>+43 123 456 7890</span></li>
        <li><svg><use href="#icon-mail"/></svg><span>email@domain.com</span></li>
        <li><svg><use href="#icon-globe"/></svg><span>www.keltostudio.com</span></li>
      </ul>
    </div>
  </section>

</main>
</body>
</html>
```